Bluegate Wound Care and Hyperbarics Website Refresh

I want to revamp my current website to be more streamlined and look cleaner. I am also adding additional service lines and another location to the company so I would like that added as well. I want to stick with the same logo and colors, but just have it cleaned up with a better overall design.

www.bghyperbarics-example.com

Target Market(s)

Wound Care and Hyperbaric Patients

Industry/Entity Type

Healthcare

Coding

Coded - Design and coding required

Number of Pages Required

5+ page

Colors
0054AA
0677BA
7BADD7
CADEEF
E8F1F8
59FF00
82FF00
B8FF75
E3FFCB
F4FFEA

```html
<!DOCTYPE html>
<html lang="en">
<head>
<meta charset="utf-8">
<title>Bluegate Wound Care &amp; Hyperbarics</title>
<link href="https://fonts.googleapis.com/css2?family=Merriweather:wght@400;700;900&family=Montserrat:wght@300;400;500;600;700&display=swap" rel="stylesheet">
<style>
:root{
  --green-dark:#1c4f2d;
  --green:#6cbd2a;
  --ink:#231f20;
  --black:#0d0d0d;
  --grey-text:#7a7a7a;
  --card-bg:#f3f3f3;
  --white:#ffffff;
  --social:#3f6fd0;
  --serif:'Merriweather', Georgia, serif;
  --sans:'Montserrat', Arial, sans-serif;
}
*{box-sizing:border-box;margin:0;padding:0}
html,body{width:1200px;height:2474px;overflow:hidden;background:var(--white);font-family:var(--sans)}
.site{position:absolute;left:93px;top:71px;width:1013px;height:2320px;box-shadow:0 10px 40px rgba(0,0,0,.18);background:var(--white)}
section,header,footer,.topbar{position:relative;width:100%}
.abs{position:absolute}

.topbar{height:28px;background:var(--ink);color:var(--white);font-size:9.5px}
.topbar .help{left:127px;top:8px;display:flex;gap:5px;align-items:center}
.topbar .help em,.topbar .hours em{color:var(--green);font-style:normal}
.topbar .hours{left:449px;top:8px;display:flex;gap:5px;align-items:center}
.topbar .social{left:819px;top:9px;display:flex;gap:10px}
.dot{width:9px;height:9px;border-radius:50%;background:var(--white);display:block}

.site-header{height:55px;background:var(--white)}
.brand{left:127px;top:14px;display:flex;align-items:center;gap:7px;font-family:var(--sans);font-weight:600;font-size:21px;letter-spacing:1px;color:var(--ink)}
.brand i{width:16px;height:16px;border-radius:50%;background:var(--green-dark);display:block}
.nav{top:22px;font-size:11px;font-weight:600;color:var(--ink)}
.btn-ask{left:781px;top:17px;width:105px;height:25px;background:var(--green);color:var(--white);font-size:9px;display:flex;align-items:center;justify-content:center}

.hero{height:392px;background:linear-gradient(100deg,#c8ccd6 0%,#b7c0d3 30%,#8fa3c4 55%,#a9a1c4 80%,#c9c2d8 100%)}
.hero-title{left:0;width:1013px;top:113px;text-align:center;font-family:var(--serif);font-weight:900;font-size:44px;color:var(--white);padding-left:46px}
.hero-sub{left:0;width:1013px;top:180px;text-align:center;font-weight:400;font-size:22px;color:var(--white);padding-left:46px}
.btn-dark{left:465px;top:221px;width:144px;height:37px;background:var(--ink);color:var(--white);font-size:11px;font-weight:700;letter-spacing:2px;display:flex;align-items:center;justify-content:center}

.intro{height:404px}
.card{top:59px;width:238px;height:284px;background:var(--card-bg);box-shadow:0 2px 8px rgba(0,0,0,.15)}
.card h3{font-family:var(--serif);font-weight:400;color:var(--green-dark)}
.card .mission{position:absolute;left:23px;top:18px;font-size:20px}
.card p{position:absolute;color:var(--grey-text);font-size:11.5px;line-height:16.2px}
.card .photo{position:absolute;left:9px;top:9px;width:221px;height:144px}
.card .name{position:absolute;left:10px;top:162px;font-size:17px}
.card .bio{left:10px;top:188px;width:220px;font-size:10.2px;line-height:16px}
.btn-green{background:var(--green);color:var(--white);font-weight:700;letter-spacing:2px;display:flex;align-items:center;justify-content:center}
.card .btn-green{position:absolute;left:21px;top:226px;width:137px;height:33px;font-size:11px}

.news{height:562px;background:var(--green-dark);color:var(--white)}
.news h2{left:0;width:1013px;top:38px;text-align:center;font-family:var(--serif);font-weight:700;font-size:33px}
.post{top:106px;width:238px}
.post .photo{width:238px;height:151px}
.post h4{margin-top:18px;padding-left:1px;font-family:var(--serif);font-weight:900;font-size:14px;line-height:19.3px;height:66px}
.post p{font-size:11px;line-height:15.5px}
.post .more{position:absolute;top:306px;left:1px;font-size:11px;font-weight:700;letter-spacing:1px;display:flex;gap:8px;align-items:center}
.news .btn-green{left:389px;top:470px;width:225px;height:44px;font-size:14px;letter-spacing:3px}

.contact{height:517px;background:linear-gradient(90deg,#4e4e4e 0%,#5d5e60 45%,#4f5456 70%,#3c4a4a 100%);color:var(--white)}
.contact h2{left:126px;top:38px;font-family:var(--serif);font-weight:400;font-size:27px;color:var(--green)}
.contact .about{left:126px;top:101px;width:360px;font-size:14.3px;line-height:17.8px}
.contact .about p+p{margin-top:18px}
.contact .kicker{left:541px;top:41px;font-family:var(--serif);font-size:17px;color:var(--green)}
.contact .lede{left:541px;top:66px;font-size:12.5px}
.contact h3{left:541px;top:94px;font-family:var(--serif);font-weight:400;font-size:21px}
.field{left:543px;width:340px;height:41px;border:2px solid var(--white);font-size:14px;padding:12px 14px}
.contact .btn-green{left:543px;top:434px;width:121px;height:42px;font-size:14px;letter-spacing:3px}

.cta{height:127px;background:linear-gradient(90deg,#7cc233 0%,#7cc233 55%,#9ad15a 75%,#8ac946 100%);color:var(--white)}
.cta h2{left:129px;top:17px;font-family:var(--serif);font-weight:700;font-size:23px}
.cta .sub{left:129px;top:44px;font-size:19px;font-weight:300}
.cta .call{left:127px;top:71px;font-family:var(--serif);font-weight:900;font-size:32px}

.site-footer{height:195px;background:var(--black);color:var(--white)}
.site-footer .brand{color:var(--white);top:31px;font-size:26px}
.site-footer .brand i{background:var(--white);width:18px;height:18px}
.site-footer .blurb{left:127px;top:101px;width:245px;font-size:9.8px;line-height:17px}
.site-footer h4{top:33px;font-family:var(--serif);font-weight:400;font-size:16.5px}
.links{left:413px;top:80px;list-style:none;font-size:11.5px}
.links li{display:flex;gap:12px;align-items:center;height:22.4px}
.detail{left:595px;display:flex;gap:12px;align-items:flex-start;font-size:13.5px}
.detail.addr{top:70px;font-size:11px;line-height:19px}
.circ{left:878px;width:17px;height:17px;border-radius:50%;background:var(--social)}
.copyright{height:40px;background:var(--black);border-top:1px solid #222;color:var(--white);font-size:11px;display:flex;align-items:center;justify-content:center}
</style>
</head>
<body>
<div class="site">

  <div class="topbar">
    <div class="abs help">
      <svg width="10" height="10" viewBox="0 0 24 24"><path d="M6.6 10.8a15 15 0 0 0 6.6 6.6l2.2-2.2a1 1 0 0 1 1-.2 11 11 0 0 0 3.6.6 1 1 0 0 1 1 1V20a1 1 0 0 1-1 1A17 17 0 0 1 3 4a1 1 0 0 1 1-1h3.5a1 1 0 0 1 1 1 11 11 0 0 0 .6 3.6 1 1 0 0 1-.3 1z" fill="#fff"/></svg>
      <span><em>Need help? Call Us Now :</em> 1800 555 0142</span>
    </div>
    <div class="abs hours">
      <svg width="10" height="10" viewBox="0 0 24 24"><circle cx="12" cy="12" r="10" fill="none" stroke="#fff" stroke-width="2.5"/><path d="M12 6v6l4 2" fill="none" stroke="#fff" stroke-width="2.5"/></svg>
      <span><em>Monday - Friday</em> | 8:00am - 5:00pm</span>
    </div>
    <div class="abs social"><i class="dot"></i><i class="dot"></i><i class="dot"></i><i class="dot"></i></div>
  </div>

  <header class="site-header">
    <div class="abs brand"><i></i>BLUEGATE</div>
    <a class="abs nav" style="left:365px">Home</a>
    <a class="abs nav" style="left:421px">About</a>
    <a class="abs nav" style="left:483px">Services</a>
    <a class="abs nav" style="left:552px">Blog</a>
    <a class="abs nav" style="left:609px">Contact us</a>
    <a class="abs btn-ask">ASK A QUESTION</a>
  </header>

  <section class="hero" role="img" aria-label="Photo of gloved hands wrapping a bandage around a patient's foot, with a clinician and stethoscope">
    <h1 class="abs hero-title">Hyperbaric Oxygen Therapy</h1>
    <p class="abs hero-sub">State of the Art Wound Care</p>
    <a class="abs btn-dark">LEARN MORE</a>
  </section>

  <section class="intro">
    <article class="abs card" style="left:127px">
      <h3 class="mission">Mission Statement</h3>
      <p style="left:23px;top:55px;width:200px">Bluegate Wound Care &amp; Hyperbarics is dedicated to the highest level of service with state of the art science for wound care. We are committed to our patient's overall wellbeing and health. We always do what is right for the patient. We will not waiver in our standard of care for our valued customers.</p>
      <a class="btn-green">MORE ABOUT US</a>
    </article>
    <article class="abs card" style="left:387px">
      <div class="photo" role="img" aria-label="Portrait of the chief executive in a blue suit standing before the clinic sign" style="background:linear-gradient(180deg,#ecebef,#dcdde3 60%,#4a6aa8 100%)"></div>
      <h3 class="name">Marcus D. Ellery</h3>
      <p class="bio">Chief Executive OfficerRealizing the need for underutilized ancillary healthcare services like hyperbaric therapy, Marcus founded Bluegate Wound Care and Hyperbarics.</p>
    </article>
    <article class="abs card" style="left:647px">
      <div class="photo" role="img" aria-label="Photo of hyperbaric chambers in a treatment room with a patient and clinicians" style="background:linear-gradient(135deg,#d7dbe3,#aeb9c8 50%,#eef0f3)"></div>
      <h3 class="name" style="top:165px">Marcus D. Ellery</h3>
      <p class="bio" style="top:191px;line-height:15px">At Bluegate, you will be treated by a highly-skilled provider, specially trained in wound care &amp; hyperbaric medicine.</p>
    </article>
  </section>

  <section class="news">
    <h2 class="abs">Latest News</h2>
    <article class="abs post" style="left:127px">
      <div class="photo" role="img" aria-label="Photo of a patient and doctor beside a hyperbaric chamber" style="background:linear-gradient(135deg,#d9b98f,#efe6da 50%,#c9a77b)"></div>
      <h4>3 Tips To Prevent Diabetic Ulcers: When To Consider Hyperbaric Therapy</h4>
      <p>People with diabetes are more prone to infected wounds and diabetic ulcers. Hyperbaric therapy can help these infections heal faster.</p>
      <span class="more">READ MORE <svg width="11" height="9" viewBox="0 0 11 9"><path d="M1 1l3.5 3.5L1 8M6 1l3.5 3.5L6 8" fill="none" stroke="#6cbd2a" stroke-width="1.6"/></svg></span>
    </article>
    <article class="abs post" style="left:387px">
      <div class="photo" role="img" aria-label="Photo of a woman holding her sore neck and shoulder" style="background:linear-gradient(160deg,#e9e2d6,#c98f6d 45%,#b9a88d)"></div>
      <h4>Autism, Cerebral Palsy &amp; Fibromyalgia: 3 Lesser-Known Reasons To Consider HBOT</h4>
      <p>Hyperbaric oxygen therapy (HBOT) provides pure oxygen in a pressurized chamber, improving conditions such as autism, cerebral palsy, and fibromyalgia.</p>
      <span class="more">READ MORE <svg width="11" height="9" viewBox="0 0 11 9"><path d="M1 1l3.5 3.5L1 8M6 1l3.5 3.5L6 8" fill="none" stroke="#6cbd2a" stroke-width="1.6"/></svg></span>
    </article>
    <article class="abs post" style="left:647px">
      <div class="photo" role="img" aria-label="Photo of a person holding their abdomen with a red highlight over the stomach" style="background:linear-gradient(135deg,#8e9299,#b56a75 50%,#7d8188)"></div>
      <h4>How Many HBOT Sessions Do I Need? Treatment For Common Conditions</h4>
      <p>HBOT continues to be an effective means of treating a range of common health issues. However, each condition needs several sessions to heal effectively.</p>
      <span class="more">READ MORE <svg width="11" height="9" viewBox="0 0 11 9"><path d="M1 1l3.5 3.5L1 8M6 1l3.5 3.5L6 8" fill="none" stroke="#6cbd2a" stroke-width="1.6"/></svg></span>
    </article>
    <a class="abs btn-green">VIEW MORE BLOG</a>
  </section>

  <section class="contact" role="img" aria-label="Dimmed photo of a clinician attending a patient in a hyperbaric chamber">
    <h2 class="abs">Wound Care at Bluegate</h2>
    <div class="abs about">
      <p>At Bluegate Wound Care &amp; Hyperbarics we are committed to the highest level of care with state of the art technology in our hyperbaric oxygen therapy clinic.&nbsp; Our stand-alone clinic offers hyperbaric medicine in a conveniently located, outpatient setting.</p>
      <p>Hyperbaric oxygen therapy (HBOT) for wound care is considered the preferred modality for many patients who are at risk with delayed wound healing.&nbsp; Wounds need oxygen to heal properly and exposing a wound to 100% oxygen can speed healing and shorten recovery time.&nbsp; In addition to aiding the healing process in wound care, HBOT has proven to be effective treating hearing issues, chronic ulcers, burn victims, injuries from radiation, migraines and some types of cancer.</p>
      <p>Bluegate Wound Care &amp; Hyperbarics are experts in oxygen therapy and hyperbaric treatments.&nbsp; Let us show you the difference today.</p>
    </div>
    <p class="abs kicker">Learn More Now!</p>
    <p class="abs lede">Let us show you the Bluegate Wound Care Difference!</p>
    <h3 class="abs">Contact Us!</h3>
    <div class="abs field" style="top:140px">Name</div>
    <div class="abs field" style="top:197px">Email</div>
    <div class="abs field" style="top:256px;height:158px">Message</div>
    <a class="abs btn-green">SEND</a>
  </section>

  <section class="cta" role="img" aria-label="Green-tinted photo of call centre staff wearing headsets">
    <h2 class="abs">Learn More Today!</h2>
    <p class="abs sub">Give us a call to schedule a consult.</p>
    <p class="abs call">Call: 469-555-0164</p>
  </section>

  <footer class="site-footer">
    <div class="abs brand"><i></i>BLUEGATE</div>
    <p class="abs blurb">Constantly looking for ways to evolve the treatment of wounds and provide services that add value to the providers who refer patients to our facilities.</p>
    <h4 class="abs" style="left:413px">Quick Links</h4>
    <ul class="abs links">
      <li><svg width="11" height="9" viewBox="0 0 11 9"><path d="M1 1l3.5 3.5L1 8M6 1l3.5 3.5L6 8" fill="none" stroke="#6cbd2a" stroke-width="1.6"/></svg>About</li>
      <li><svg width="11" height="9" viewBox="0 0 11 9"><path d="M1 1l3.5 3.5L1 8M6 1l3.5 3.5L6 8" fill="none" stroke="#6cbd2a" stroke-width="1.6"/></svg>Services</li>
      <li><svg width="11" height="9" viewBox="0 0 11 9"><path d="M1 1l3.5 3.5L1 8M6 1l3.5 3.5L6 8" fill="none" stroke="#6cbd2a" stroke-width="1.6"/></svg>Blog</li>
      <li><svg width="11" height="9" viewBox="0 0 11 9"><path d="M1 1l3.5 3.5L1 8M6 1l3.5 3.5L6 8" fill="none" stroke="#6cbd2a" stroke-width="1.6"/></svg>Contact us</li>
    </ul>
    <h4 class="abs" style="left:595px">Contact Details</h4>
    <div class="abs detail addr">
      <svg width="15" height="19" viewBox="0 0 24 30"><path d="M12 0a10 10 0 0 0-10 10c0 8 10 20 10 20s10-12 10-20A10 10 0 0 0 12 0zm0 14a4 4 0 1 1 0-8 4 4 0 0 1 0 8z" fill="#6cbd2a"/></svg>
      <span>Address: 4820 Parkline Rd, Suite 210,<br>Irving, TX 75039</span>
    </div>
    <div class="abs detail" style="top:124px">
      <svg width="17" height="17" viewBox="0 0 24 24"><path d="M6.6 10.8a15 15 0 0 0 6.6 6.6l2.2-2.2a1 1 0 0 1 1-.2 11 11 0 0 0 3.6.6 1 1 0 0 1 1 1V20a1 1 0 0 1-1 1A17 17 0 0 1 3 4a1 1 0 0 1 1-1h3.5a1 1 0 0 1 1 1 11 11 0 0 0 .6 3.6 1 1 0 0 1-.3 1z" fill="#6cbd2a"/></svg>
      <span>469-555-0164</span>
    </div>
    <div class="abs detail" style="top:153px">
      <svg width="18" height="17" viewBox="0 0 24 22"><rect x="6" y="0" width="12" height="6" fill="#6cbd2a"/><rect x="0" y="7" width="24" height="10" rx="2" fill="#6cbd2a"/><rect x="6" y="13" width="12" height="9" fill="#6cbd2a" stroke="#0d0d0d" stroke-width="1.5"/></svg>
      <span>469-555-0135</span>
    </div>
    <i class="abs circ" style="top:48px"></i>
    <i class="abs circ" style="top:73px"></i>
    <i class="abs circ" style="top:97px"></i>
    <i class="abs circ" style="top:122px"></i>
  </footer>

  <div class="copyright">© Copyright 2022 | All Rights Reserved</div>
</div>
</body>
</html>
```